Pelmar Social "is a company that is focused on managing social media platforms.

I need a website design for a social media management company. The owner is a social media influencer in the Denver, Co area. Would like IG and Tik Tok page intergraded into the site. Would like all post from social to go directly to new website. Also put a page link for blog: her is my blog https://www.quillorin.com/about

Target Market(s)

Any business that needs social media managed or video made for their company.

Coding

Coded - Design and coding required

Requirements
Must have
• Color scheme needs to match logo ; • IG: https://www.examplegram.com/quil.orin/ • Exampletok: https://www.exampletok.com/@quil.orin Please add these videos: https://fx.tl/b-qRtM4Wnpzx
Nice to have
• • https://greenowlstudio.co/ "this a website that i like in the industry"

```html
<!DOCTYPE html>
<html lang="en">
<head>
<meta charset="utf-8">
<title>Pelmar Social — Your Social Media, Done Right</title>
<link href="https://fonts.googleapis.com/css2?family=Poppins:wght@300;400;500;600;700&display=swap" rel="stylesheet">
<style>
:root{
  --navy:#0c1f44;
  --navy-deep:#0b1d3d;
  --royal:#0a2a8c;
  --ink:#111827;
  --muted:#4b5563;
  --line:#1e3a8a;
  --accent:#2563eb;
  --mist:#eef1f4;
  --peach:#f9e2d6;
  --sky:#bfd7f3;
  --cream:#f8e6cc;
  --white:#ffffff;
}
*{margin:0;padding:0;box-sizing:border-box}
html,body{width:1200px;height:3829px;overflow:hidden;background:var(--white)}
body{font-family:'Poppins',sans-serif;color:var(--ink)}
.page{position:relative;width:1200px;height:3829px;overflow:hidden}
.abs{position:absolute}
a{color:inherit;text-decoration:none}
.photo{position:absolute;overflow:hidden}
.btn-dark{position:absolute;background:var(--navy);color:var(--white);font-size:10px;font-weight:600;display:flex;align-items:center;justify-content:center;letter-spacing:.3px}
.section-title{position:absolute;left:0;width:1200px;display:flex;justify-content:center;align-items:center;gap:12px;font-weight:500;color:var(--ink)}
.section-title::before,.section-title::after{content:"";width:74px;height:2px;background:var(--ink)}
.arrow{position:absolute;width:30px;height:30px;border:1px solid var(--ink);border-radius:50%;display:flex;align-items:center;justify-content:center;background:var(--white)}

/* hero */
.hero{position:absolute;left:0;top:0;width:1200px;height:597px;background:linear-gradient(100deg,#dcd4cc 0%,#c6cfe6 30%,#b4c9f1 55%,#b9cdf0 75%,#d7d2cf 100%)}
.brand-box{position:absolute;left:122px;top:7px;width:113px;height:84px;background:var(--navy);display:flex;align-items:center;justify-content:center;color:var(--white);font-size:11px;font-weight:500;letter-spacing:2px;text-align:center;line-height:1.5}
.nav{position:absolute;top:22px;left:624px;display:flex;font-size:10.5px;font-weight:500;color:var(--ink)}
.nav a{position:absolute;white-space:nowrap}
.nav .active{color:var(--accent);border-bottom:1px solid var(--accent)}
.eyebrow{position:absolute;font-size:14px;font-weight:400;display:flex;align-items:center;gap:10px}
.eyebrow::after{content:"";width:30px;height:1px;background:var(--ink)}
.hero h1{position:absolute;left:122px;top:226px;font-size:36px;font-weight:500;line-height:44px;color:var(--ink)}
.hero p{position:absolute;left:122px;top:318px;width:395px;font-size:10.5px;line-height:17px;color:var(--ink)}
.social-dot{position:absolute;border-radius:50%;box-shadow:0 4px 10px rgba(0,0,0,.25)}
.mini-card{position:absolute;background:var(--white);border-radius:8px;box-shadow:0 4px 12px rgba(0,0,0,.2);padding:8px}

/* about */
.about-frame{position:absolute;left:123px;top:662px;width:390px;height:358px;border:2px solid var(--line);border-radius:14px;background:#fbf3ea}
.about h2{position:absolute;left:622px;top:752px;font-size:29px;font-weight:500;line-height:38px;color:var(--ink)}
.outline-word{position:absolute;left:-12px;top:1010px;font-size:176px;font-weight:300;line-height:1;white-space:nowrap;color:transparent;-webkit-text-stroke:1.2px var(--navy);letter-spacing:4px}

/* services */
.services{position:absolute;left:0;top:1163px;width:1200px;height:468px;background:var(--mist)}
.svc{position:absolute;top:146px;width:224px;height:258px;border-radius:12px;background:linear-gradient(160deg,var(--peach) 0%,#ecdde0 40%,var(--sky) 100%);text-align:center}
.svc .ico{position:absolute;left:80px;top:17px;width:64px;height:64px;border-radius:50%;background:var(--white);border:1.5px solid var(--ink);display:flex;align-items:center;justify-content:center}
.svc h3{position:absolute;top:102px;width:100%;font-size:14px;font-weight:600}
.svc p{position:absolute;top:128px;left:14px;width:196px;font-size:10px;line-height:16px;color:#374151}
.svc .more{position:absolute;top:199px;left:59px;width:107px;height:36px;border:1px solid var(--line);font-size:10px;font-weight:500;color:var(--line);display:flex;align-items:center;justify-content:center}

/* why */
.why-card{position:absolute;top:1796px;width:180px;height:119px;border:1.5px solid #6b8fd6;border-radius:6px;background:var(--white);text-align:center}
.why-card.on{background:var(--navy);border-color:var(--navy);color:var(--white)}
.why-card .ico{position:absolute;left:58px;top:-22px;width:64px;height:64px;border-radius:50%;background:var(--white);border:1.5px solid var(--ink);display:flex;align-items:center;justify-content:center}
.why-card span{position:absolute;top:44px;left:0;width:100%;font-size:14px;line-height:18px}

/* portfolio */
.portfolio{position:absolute;left:0;top:1987px;width:1200px;height:397px;background:linear-gradient(180deg,#c6e6fb,#d4ecfb 60%,#c2e2fa)}
.portfolio .section-title::before,.portfolio .section-title::after{width:92px;background:var(--accent)}

/* testimonials */
.quote-card{position:absolute;top:2522px;height:239px;border-radius:14px;background:linear-gradient(120deg,#c9dcf4 0%,#e8e2e6 55%,var(--peach) 100%)}
.quote-card blockquote{position:absolute;left:26px;top:78px;width:420px;font-size:15.5px;line-height:23px;color:#1f2937}
.quote-card .who{position:absolute;left:30px;top:176px;display:flex;align-items:center;gap:12px}
.avatar{width:46px;height:46px;border-radius:50%;background:linear-gradient(135deg,#c9ccd4,#3b4254)}
.stars{color:#f5b400;font-size:10px;letter-spacing:1px}
.who small{display:block;font-size:9.5px;font-weight:500;color:var(--ink)}

/* blog */
.blog{position:absolute;left:0;top:2825px;width:1200px;height:473px;background:#eef0f3}
.post{position:absolute;top:137px;width:307px}
.post .frame{position:relative;width:307px;height:214px;border:1.5px solid var(--line);border-radius:10px;padding:6px;background:var(--white)}
.post .frame .photo{left:6px;top:6px;right:6px;bottom:6px;border-radius:8px}
.post h4{position:absolute;left:0;top:226px;font-size:17.5px;font-weight:600}
.post time{position:absolute;right:0;top:231px;font-size:10.5px;color:#374151}
.post a{position:absolute;left:0;top:262px;font-size:10.5px;font-weight:600;text-decoration:underline;display:flex;align-items:center;gap:6px}

/* cta */
.cta{position:absolute;left:0;top:3298px;width:1200px;height:214px;background:radial-gradient(ellipse at 50% 40%,#0d37b0,var(--royal) 60%,#08227a)}
.cta h2{position:absolute;top:50px;width:100%;text-align:center;color:var(--white);font-size:34px;font-weight:600;letter-spacing:.5px}

/* footer */
.footer{position:absolute;left:0;top:3512px;width:1200px;height:317px;background:var(--navy-deep);color:var(--white)}
.footer h5{position:absolute;font-size:14px;font-weight:500;letter-spacing:.3px}
.footer ul{position:absolute;list-style:none;font-size:11px}
.footer ul li{height:26.5px}
.contact-row{position:absolute;left:622px;display:flex;align-items:center;gap:8px;font-size:11px}
.contact-row i{width:16px;height:16px;border:1px solid var(--white);border-radius:2px;display:flex;align-items:center;justify-content:center}
</style>
</head>
<body>
<div class="page">

  <!-- HERO -->
  <header class="hero">
    <div class="brand-box">PELMAR<br>SOCIAL</div>
    <nav class="nav">
      <a class="active" style="left:0">HOME</a>
      <a style="left:62px">ABOUT US</a>
      <a style="left:146px">WHAT WE DO</a>
      <a style="left:249px">STORIES</a>
      <a style="left:323px">BLOG</a>
    </nav>
    <a class="btn-dark" style="left:1002px;top:15px;width:75px;height:30px">LOG IN</a>

    <div class="eyebrow" style="left:122px;top:197px">WELCOME TO PELMAR SOCIAL</div>
    <h1>YOUR SOCIAL MEDIA,<br>DONE RIGHT</h1>
    <p>At Pelmar Social, we help you build a bold digital presence with smart strategy, beautiful content, and meaningful engagement. From daily posts to full-scale campaigns, we manage your social media so you can focus on running your business.</p>
    <a class="btn-dark" style="left:122px;top:416px;width:123px;height:35px">EXPLORE NOW</a>

    <div class="photo" role="img" aria-label="Portrait of the founder standing on a city balcony with a handbag" style="left:666px;top:144px;width:354px;height:363px;border:2px solid var(--line);border-radius:8px;background:linear-gradient(160deg,#5a5048,#2f2a28 45%,#786f66)"></div>
    <div class="social-dot" style="left:976px;top:126px;width:64px;height:64px;background:var(--white);border:2px solid var(--line)"></div>
    <div class="social-dot" style="left:625px;top:200px;width:52px;height:52px;background:var(--navy)"></div>

    <div class="mini-card" style="left:522px;top:357px;width:118px;height:40px;display:flex;align-items:center;gap:4px;padding:0 10px">
      <span style="width:14px;height:14px;border-radius:50%;background:#b58f7a"></span>
      <span style="width:14px;height:14px;border-radius:50%;background:#a77"></span>
      <span style="width:14px;height:14px;border-radius:50%;background:#8a8"></span>
      <span style="width:14px;height:14px;border-radius:50%;background:#c96"></span>
      <span style="width:14px;height:14px;border-radius:50%;background:#333"></span>
    </div>
    <svg class="abs" style="left:610px;top:395px" width="66" height="58" viewBox="0 0 66 58" fill="none" stroke="#1e3a8a" stroke-width="2">
      <path d="M16 2 C0 14 8 30 20 26 C30 22 22 10 14 18 C6 28 20 46 58 46"/>
      <path d="M52 40 L60 46 L52 52"/>
    </svg>

    <div class="mini-card" style="left:944px;top:437px;width:133px;height:101px">
      <div style="display:flex;gap:6px;align-items:center">
        <span style="width:18px;height:18px;border-radius:50%;background:#8a7f78"></span>
        <span style="width:50px;height:14px;background:repeating-linear-gradient(180deg,#cbd0d8 0 2px,transparent 2px 5px)"></span>
      </div>
      <div style="display:flex;gap:4px;margin-top:8px">
        <span style="width:11px;height:11px;border-radius:50%;background:#555"></span><span style="width:11px;height:11px;border-radius:50%;background:#a66"></span><span style="width:11px;height:11px;border-radius:50%;background:#765"></span><span style="width:11px;height:11px;border-radius:50%;background:#977"></span><span style="width:11px;height:11px;border-radius:50%;background:#c85"></span><span style="width:11px;height:11px;border-radius:50%;background:#444"></span>
      </div>
      <div role="img" aria-label="Grid of recent social posts" style="margin-top:8px;height:34px;background:linear-gradient(90deg,#3a3a3a,#b0623b 40%,#3d5a88 70%,#c07a55)"></div>
    </div>
  </header>

  <!-- ABOUT -->
  <section class="about">
    <div class="about-frame">
      <div class="photo" role="img" aria-label="Founder posing at an evening event under warm string lights" style="left:10px;top:10px;width:366px;height:334px;border-radius:10px;background:radial-gradient(ellipse at 55% 60%,#6b4630,#3a2418 55%,#1e130d)"></div>
      <div class="abs" style="left:164px;top:151px;width:60px;height:60px;border-radius:50%;background:rgba(220,220,220,.55);display:flex;align-items:center;justify-content:center">
        <svg width="24" height="26" viewBox="0 0 24 26"><path d="M4 2 L22 13 L4 24 Z" fill="#1e3a8a"/></svg>
      </div>
    </div>
    <div class="mini-card" style="left:445px;top:706px;width:133px;height:104px">
      <div style="display:flex;gap:6px;align-items:center">
        <span style="width:18px;height:18px;border-radius:50%;background:#8a7f78"></span>
        <span style="width:50px;height:14px;background:repeating-linear-gradient(180deg,#cbd0d8 0 2px,transparent 2px 5px)"></span>
      </div>
      <div style="display:flex;gap:4px;margin-top:8px">
        <span style="width:11px;height:11px;border-radius:50%;background:#555"></span><span style="width:11px;height:11px;border-radius:50%;background:#a66"></span><span style="width:11px;height:11px;border-radius:50%;background:#765"></span><span style="width:11px;height:11px;border-radius:50%;background:#977"></span><span style="width:11px;height:11px;border-radius:50%;background:#c85"></span><span style="width:11px;height:11px;border-radius:50%;background:#444"></span>
      </div>
      <div role="img" aria-label="Grid of recent social posts" style="margin-top:8px;height:34px;background:linear-gradient(90deg,#3a3a3a,#b0623b 40%,#3d5a88 70%,#c07a55)"></div>
    </div>
    <svg class="abs" style="left:526px;top:800px" width="60" height="52" viewBox="0 0 60 52" fill="none" stroke="#1e3a8a" stroke-width="2">
      <path d="M52 4 C62 28 44 48 14 42"/><path d="M20 35 L12 42 L20 49"/>
    </svg>

    <div class="eyebrow" style="left:622px;top:722px;font-size:10.5px;gap:16px"><span>ABOUT US</span></div>
    <div class="abs" style="left:688px;top:731px;width:74px;height:1px;background:var(--ink)"></div>
    <h2>ELEVATE YOUR SOCIAL<br>PRESENCEWITH PELMAR SOCIAL</h2>
    <p class="abs" style="left:622px;top:837px;font-size:11px;font-weight:600">Your trusted partner for impactful, stress-free social media management.</p>
    <p class="abs" style="left:622px;top:864px;width:440px;font-size:10.5px;line-height:14px">At <b>Pelmar Social</b>, we help brands rise above the noise. From bold visuals to data-backed strategies, we handle every aspect of your social media presence with precision and passion.</p>
    <a class="btn-dark" style="left:622px;top:935px;width:105px;height:35px">LEARN MORE</a>
    <div class="outline-word" aria-hidden="true">PELMAR SOCIAL</div>
  </section>

  <!-- WHAT WE DO -->
  <section class="services">
    <h2 class="section-title" style="top:56px;font-size:28px">WHAT WE DO</h2>
    <div class="arrow" style="left:68px;top:264px"><svg width="12" height="10" viewBox="0 0 12 10" fill="none" stroke="#111" stroke-width="1.3"><path d="M11 5H1M5 1L1 5L5 9"/></svg></div>
    <div class="arrow" style="left:1100px;top:264px"><svg width="12" height="10" viewBox="0 0 12 10" fill="none" stroke="#111" stroke-width="1.3"><path d="M1 5H11M7 1L11 5L7 9"/></svg></div>

    <article class="svc" style="left:122px">
      <div class="ico"><svg width="32" height="32" viewBox="0 0 32 32" fill="none" stroke="#111" stroke-width="1.8"><rect x="3" y="3" width="11" height="11"/><rect x="18" y="3" width="11" height="11"/><rect x="3" y="18" width="11" height="11"/><rect x="18" y="18" width="11" height="11"/></svg></div>
      <h3>Examplegram Management</h3>
      <p>Grow your presence with stunning visuals, engaging captions, and optimized posting strategies.</p>
      <a class="more">LEARN MORE</a>
    </article>
    <article class="svc" style="left:366px">
      <div class="ico"><svg width="34" height="34" viewBox="0 0 34 34" fill="none" stroke="#111" stroke-width="2"><rect x="7" y="3" width="20" height="28" rx="3"/><path d="M14 26h6"/></svg></div>
      <h3>Exampletok Management</h3>
      <p>Trendy, creative, and on-brand short-form videos that get attention and spark engagement.</p>
      <a class="more">LEARN MORE</a>
    </article>
    <article class="svc" style="left:610px">
      <div class="ico"><svg width="34" height="34" viewBox="0 0 34 34" fill="none" stroke="#111" stroke-width="1.8"><rect x="9" y="2" width="16" height="30" rx="3"/><rect x="4" y="9" width="10" height="7" rx="1"/><rect x="20" y="18" width="10" height="7" rx="1"/><path d="M14 22h3"/></svg></div>
      <h3>Social Media Strategy</h3>
      <p>Custom plans built around your goals, audience insights, and competitive analysis.</p>
      <a class="more">LEARN MORE</a>
    </article>
    <article class="svc" style="left:854px">
      <div class="ico"><svg width="34" height="34" viewBox="0 0 34 34" fill="none" stroke="#111" stroke-width="1.8"><rect x="3" y="5" width="28" height="19" rx="2"/><path d="M13 30h8M17 24v6M10 18l8-8 3 3-8 8h-3z"/></svg></div>
      <h3>Content Creation</h3>
      <p>Branded graphics, reels, stories, and captions that stop the scroll and build recognition.</p>
      <a class="more">LEARN MORE</a>
    </article>
  </section>

  <!-- WHY CHOOSE -->
  <h2 class="section-title" style="top:1684px;font-size:28px">WHY CHOOSE PELMAR SOCIAL?</h2>
  <div class="arrow" style="left:68px;top:1839px"><svg width="12" height="10" viewBox="0 0 12 10" fill="none" stroke="#111" stroke-width="1.3"><path d="M11 5H1M5 1L1 5L5 9"/></svg></div>
  <div class="arrow" style="left:1100px;top:1839px"><svg width="12" height="10" viewBox="0 0 12 10" fill="none" stroke="#111" stroke-width="1.3"><path d="M1 5H11M7 1L11 5L7 9"/></svg></div>
  <div class="why-card" style="left:120px"><div class="ico"><svg width="30" height="30" viewBox="0 0 30 30" fill="none" stroke="#111" stroke-width="1.6"><rect x="9" y="3" width="12" height="24" rx="2"/><path d="M13 11l4 3-4 3z"/><path d="M5 10c-2 3-2 7 0 10M25 10c2 3 2 7 0 10"/></svg></div><span>Examplegram &amp;<br>Exampletok Experts</span></div>
  <div class="why-card on" style="left:314px"><div class="ico"><svg width="30" height="30" viewBox="0 0 30 30" fill="none" stroke="#111" stroke-width="1.6"><rect x="6" y="3" width="14" height="24" rx="2"/><path d="M10 13h6M10 17h4"/><rect x="19" y="14" width="8" height="7" rx="1"/></svg></div><span>Influencer<br>Led Insight</span></div>
  <div class="why-card" style="left:507px"><div class="ico"><svg width="30" height="30" viewBox="0 0 30 30" fill="none" stroke="#111" stroke-width="1.6"><rect x="4" y="4" width="22" height="22" rx="2"/><path d="M8 22v-4M12 22v-7M16 22v-5M20 22v-9M8 13l5-4 4 3 6-5"/></svg></div><span>Strategy<br>First Approach</span></div>
  <div class="why-card" style="left:700px"><div class="ico"><svg width="30" height="30" viewBox="0 0 30 30" fill="none" stroke="#111" stroke-width="1.6"><circle cx="15" cy="15" r="11"/><path d="M4 15h22M15 4c-5 6-5 16 0 22M15 4c5 6 5 16 0 22"/></svg></div><span>Local Roots,<br>National Reach</span></div>
  <div class="why-card" style="left:895px"><div class="ico"><svg width="30" height="30" viewBox="0 0 30 30" fill="none" stroke="#111" stroke-width="1.6"><path d="M7 12c0-6 16-6 16 0"/><rect x="10" y="12" width="10" height="7" rx="2"/><path d="M5 26c2-5 18-5 20 0z"/></svg></div><span>Personalized<br>Service</span></div>

  <!-- PORTFOLIO -->
  <section class="portfolio">
    <h2 class="section-title" style="top:56px;font-size:32px">OUR PORTFOLIO</h2>
    <div class="arrow" style="left:68px;top:227px"><svg width="12" height="10" viewBox="0 0 12 10" fill="none" stroke="#111" stroke-width="1.3"><path d="M11 5H1M5 1L1 5L5 9"/></svg></div>
    <div class="arrow" style="left:1100px;top:227px"><svg width="12" height="10" viewBox="0 0 12 10" fill="none" stroke="#111" stroke-width="1.3"><path d="M1 5H11M7 1L11 5L7 9"/></svg></div>
    <div class="photo" role="img" aria-label="Outfit photo in a white interior, cream top and trousers" style="left:122px;top:150px;width:143px;height:184px;border-radius:8px;background:linear-gradient(180deg,#e6e4df,#bcb3a6)"></div>
    <div class="photo" role="img" aria-label="Lavender gown at an outdoor garden venue" style="left:284px;top:150px;width:143px;height:184px;border-radius:8px;background:linear-gradient(180deg,#8fa3a5,#7d6fb4 60%,#6a7e55)"></div>
    <div class="photo" role="img" aria-label="Blue halter dress in front of green hedges" style="left:446px;top:150px;width:143px;height:184px;border-radius:8px;background:linear-gradient(180deg,#4c5a3e,#334c9a 60%,#5a5a52)"></div>
    <div class="photo" role="img" aria-label="Black tailored suit against a white door" style="left:609px;top:150px;width:143px;height:184px;border-radius:8px;background:linear-gradient(180deg,#d8d6d2,#2a2a2d 70%)"></div>
    <div class="photo" role="img" aria-label="White mini outfit in a home kitchen" style="left:771px;top:150px;width:143px;height:184px;border-radius:8px;background:linear-gradient(180deg,#a88f72,#e9e2d8 55%,#8b7155)"></div>
    <div class="photo" role="img" aria-label="Cream knit set at a dimly lit restaurant" style="left:934px;top:150px;width:143px;height:184px;border-radius:8px;background:linear-gradient(180deg,#3a2016,#cdbfb0 55%,#4a2a1c)"></div>
  </section>

  <!-- TESTIMONIALS -->
  <h2 class="section-title" style="top:2436px;font-size:34px">CLIENT TESTIMONIALS</h2>
  <div class="arrow" style="left:68px;top:2627px"><svg width="12" height="10" viewBox="0 0 12 10" fill="none" stroke="#111" stroke-width="1.3"><path d="M11 5H1M5 1L1 5L5 9"/></svg></div>
  <div class="arrow" style="left:1100px;top:2627px"><svg width="12" height="10" viewBox="0 0 12 10" fill="none" stroke="#111" stroke-width="1.3"><path d="M1 5H11M7 1L11 5L7 9"/></svg></div>
  <article class="quote-card" style="left:120px;width:469px">
    <svg class="abs" style="left:26px;top:20px" width="60" height="42" viewBox="0 0 60 42" fill="#9aa8bd"><path d="M2 42V20C2 8 10 2 24 0v8c-7 2-10 6-10 12h10v22zM34 42V20C34 8 42 2 56 0v8c-7 2-10 6-10 12h10v22z"/></svg>
    <blockquote>“Pelmar Social completely transformed our Examplegram presence. Engagement is up 300%, and our DMs are constantly full of inquiries.”</blockquote>
    <div class="who"><div class="avatar" role="img" aria-label="Client headshot"></div><div><div class="stars">★★★★★</div><small>Dana Moore, Owner, The Ridgeline Floral Co.</small></div></div>
  </article>
  <article class="quote-card" style="left:610px;width:467px">
    <svg class="abs" style="left:26px;top:20px" width="60" height="42" viewBox="0 0 60 42" fill="#9aa8bd"><path d="M2 42V20C2 8 10 2 24 0v8c-7 2-10 6-10 12h10v22zM34 42V20C34 8 42 2 56 0v8c-7 2-10 6-10 12h10v22z"/></svg>
    <blockquote>“They just get the Exampletok space. Their video content helped us go viral more than once—and the new followers keep coming.”</blockquote>
    <div class="who"><div class="avatar" role="img" aria-label="Client headshot"></div><div><div class="stars">★★★★★</div><small>Theo L., Marketing Director, Brightleaf Wellness</small></div></div>
  </article>

  <!-- BLOG -->
  <section class="blog">
    <h2 class="abs" style="left:122px;top:52px;font-size:32px;font-weight:500;display:flex;align-items:center;gap:12px">OUR BLOG <span style="width:88px;height:2px;background:var(--ink)"></span></h2>
    <a class="btn-dark" style="left:965px;top:61px;width:112px;height:34px">VIEW ALL BLOG</a>
    <div class="arrow" style="left:68px;top:232px"><svg width="12" height="10" viewBox="0 0 12 10" fill="none" stroke="#111" stroke-width="1.3"><path d="M11 5H1M5 1L1 5L5 9"/></svg></div>
    <div class="arrow" style="left:1100px;top:232px"><svg width="12" height="10" viewBox="0 0 12 10" fill="none" stroke="#111" stroke-width="1.3"><path d="M1 5H11M7 1L11 5L7 9"/></svg></div>
    <article class="post" style="left:122px">
      <div class="frame"><div class="photo" role="img" aria-label="Brown jumpsuit with faux fur coat indoors" style="background:linear-gradient(180deg,#5a3a26,#2a1d18 50%,#6b4a34)"></div></div>
      <h4>Brown Jumpsuit</h4><time>April 3, 2025</time>
      <a>Read More <svg width="12" height="8" viewBox="0 0 12 8" fill="none" stroke="#111" stroke-width="1.2"><path d="M0 4h11M8 1l3 3-3 3"/></svg></a>
    </article>
    <article class="post" style="left:446px">
      <div class="frame"><div class="photo" role="img" aria-label="Pale blue two-piece set beside a reflecting pond" style="background:linear-gradient(180deg,#7e8a86,#4f5a52 50%,#98a6b2)"></div></div>
      <h4>Blue Lunara Set</h4><time>April 3, 2025</time>
      <a>Read More <svg width="12" height="8" viewBox="0 0 12 8" fill="none" stroke="#111" stroke-width="1.2"><path d="M0 4h11M8 1l3 3-3 3"/></svg></a>
    </article>
    <article class="post" style="left:770px">
      <div class="frame"><div class="photo" role="img" aria-label="Two cocktails held in hands at a seafood bar" style="background:linear-gradient(90deg,#8a1e1a,#c04a30 40%,#c8b58a 70%,#3a2a22)"></div></div>
      <h4>Marino Seafood Bar</h4><time>January 29, 2025</time>
      <a>Read More <svg width="12" height="8" viewBox="0 0 12 8" fill="none" stroke="#111" stroke-width="1.2"><path d="M0 4h11M8 1l3 3-3 3"/></svg></a>
    </article>
  </section>

  <!-- CTA -->
  <section class="cta">
    <h2>READY TO GROW YOUR SOCIAL?</h2>
    <a class="abs" style="left:526px;top:118px;width:149px;height:31px;background:var(--cream);color:var(--ink);font-size:10px;font-weight:600;display:flex;align-items:center;justify-content:center">CONTACT US TODAY!</a>
  </section>

  <!-- FOOTER -->
  <footer class="footer">
    <div class="abs" style="left:171px;top:58px;width:60px;height:60px;border:1.5px solid var(--white)"></div>
    <div class="abs" style="left:120px;top:133px;font-size:13px;letter-spacing:5px">PELMAR SOCIAL</div>
    <h5 style="left:122px;top:164px">FOLLOW US</h5>
    <div class="abs" style="left:122px;top:191px;display:flex;gap:14px">
      <span style="width:26px;height:22px;border:1px solid var(--white)"></span>
      <span style="width:26px;height:22px;border:1px solid var(--white)"></span>
      <span style="width:26px;height:22px;border:1px solid var(--white)"></span>
    </div>

    <h5 style="left:418px;top:60px">QUICK LINKS</h5>
    <ul style="left:418px;top:94px"><li>HOME</li><li>ABOUT US</li><li>WHAT WE DO</li><li>STORIES</li><li>BLOG</li></ul>

    <h5 style="left:622px;top:58px">CONTACT INFO</h5>
    <div class="contact-row" style="top:93px"><i><svg width="10" height="10" viewBox="0 0 10 10" fill="none" stroke="#fff"><path d="M2 1l2 2-1 1.5c1 1.5 2 2.5 3.5 3.5L8 7l2 2-1.5 1C5 10 0 5 0 2.5z"/></svg></i>+ 123-456-789</div>
    <div class="contact-row" style="top:123px"><i><svg width="10" height="8" viewBox="0 0 10 8" fill="none" stroke="#fff"><rect x=".5" y=".5" width="9" height="7"/><path d="M.5 .5l4.5 4 4.5-4"/></svg></i>Pelmar Social@.com</div>
    <div class="contact-row" style="top:153px"><i><svg width="10" height="10" viewBox="0 0 10 10" fill="none" stroke="#fff"><circle cx="5" cy="5" r="4.5"/><path d="M.5 5h9M5 .5v9"/></svg></i>Pelmar Social.com</div>

    <h5 style="left:867px;top:60px">NEWSLETTER SIGNUP</h5>
    <div class="abs" style="left:867px;top:97px;width:211px;height:33px;border:1px solid var(--white);font-size:10px;display:flex;align-items:center;padding-left:12px">Email</div>
    <div class="abs" style="left:867px;top:136px;width:211px;height:32px;background:var(--cream);color:var(--ink);font-size:10px;font-weight:600;display:flex;align-items:center;justify-content:center">SUBSCRIBE</div>

    <div class="abs" style="left:122px;top:250px;width:956px;height:1px;background:rgba(255,255,255,.6)"></div>
    <div class="abs" style="left:122px;top:260px;font-size:10px">Copyright © 2025 Pelmar Social All rights reserved.</div>
    <div class="abs" style="left:827px;top:260px;font-size:10px;display:flex;gap:14px"><span>Company</span><span>Privacy Policy</span><span>Terms and Conditions</span></div>
  </footer>
</div>
</body>
</html>
```